Business Card Design

I need a Business Card that will catch the attention that will not get thrown in a Drawer. I have 23 companies I use for Auto, Home, Life, and Business Insurance. I make sure that people have the best coverage for the $ spent.

Industry/Entity Type

Business

Contact Information for Business Card

Dorlin Insurance Agency, Inc., Marcus Helgren, 4375 West Tamber Lane Brenton Falls, Vermont 45192 555-281-7496, www.dorlinagency.example, Facebook, LinkedIn, Google+

```html
<!DOCTYPE html>
<html lang="en">
<head>
<meta charset="utf-8">
<title>Dorlin Insurance Agency – Business Card</title>
<link href="https://fonts.googleapis.com/css2?family=Questrial&display=swap" rel="stylesheet">
<style>
  :root {
    --backdrop: #a8a8a8;
    --card-top: #0c0c0d;
    --card-mid: #1d1e20;
    --card-bottom: #0a0a0b;
    --silver-light: #f2f2f2;
    --silver-dark: #8d8d8d;
    --brand-silver: #c9c9c9;
    --name-blue: #1f72b8;
    --icon-blue: #2a86cf;
    --text-white: #f4f4f4;
    --ring-blue: #2f7fc4;
  }
  * { margin: 0; padding: 0; box-sizing: border-box; }
  html, body {
    width: 1200px; height: 900px; overflow: hidden;
    background: var(--backdrop);
    font-family: "Questrial", "Century Gothic", sans-serif;
  }
  .business-card {
    position: absolute; left: 100px; top: 170px;
    width: 1000px; height: 560px;
    border-radius: 44px;
    background: linear-gradient(160deg, var(--card-top) 0%, var(--card-mid) 45%, var(--card-bottom) 100%);
    box-shadow: 0 18px 40px rgba(0,0,0,0.35);
    overflow: hidden;
  }
  .brand {
    position: absolute; left: 70px; top: 48px;
    display: flex; align-items: center; gap: 36px;
  }
  .brand-mark {
    width: 200px; height: 200px; border-radius: 50%;
    border: 12px solid var(--ring-blue);
  }
  .brand-name {
    font-size: 42px; color: var(--brand-silver); letter-spacing: -0.5px; white-space: nowrap;
  }
  .silver-band {
    position: absolute; left: 0; right: 0; top: 292px; height: 10px;
    background: linear-gradient(180deg, var(--silver-light), var(--silver-dark));
  }
  .agent-name {
    position: absolute; left: 62px; top: 330px;
    font-size: 38px; color: var(--name-blue);
  }
  .contact-list {
    position: absolute; left: 68px; top: 400px; list-style: none;
    color: var(--text-white); font-size: 26px; line-height: 34px;
  }
  .contact-list li { display: flex; align-items: flex-start; gap: 14px; }
  .contact-list svg { width: 26px; height: 26px; margin-top: 4px; flex: none; fill: var(--icon-blue); }
  .contact-list svg.globe-icon { fill: none; stroke: var(--icon-blue); stroke-width: 2; }
  .contact-list .indent { padding-left: 40px; }
  .social-links {
    position: absolute; right: 62px; top: 428px; display: flex; gap: 6px;
  }
  .social-links span {
    width: 28px; height: 28px; border-radius: 4px;
    background: linear-gradient(180deg, #3a7bc8, #1d5a9e);
  }
  .social-links span:nth-child(2) { background: linear-gradient(180deg, #e0523e, #b7301f); }
</style>
</head>
<body>
  <div class="business-card">
    <div class="brand">
      <div class="brand-mark"></div>
      <div class="brand-name">Dorlin Insurance Agency, Inc.</div>
    </div>
    <div class="silver-band"></div>
    <div class="agent-name">Marcus Helgren</div>
    <ul class="contact-list">
      <li>
        <svg viewBox="0 0 24 24" aria-hidden="true"><path d="M6.6 10.8a15.1 15.1 0 0 0 6.6 6.6l2.2-2.2a1 1 0 0 1 1-.25 11.4 11.4 0 0 0 3.6.57 1 1 0 0 1 1 1V20a1 1 0 0 1-1 1A17 17 0 0 1 3 4a1 1 0 0 1 1-1h3.5a1 1 0 0 1 1 1c0 1.25.2 2.45.57 3.57a1 1 0 0 1-.25 1z"/></svg>
        <span>555-281-7496,</span>
      </li>
      <li>
        <svg class="globe-icon" viewBox="0 0 24 24" aria-hidden="true"><circle cx="12" cy="12" r="9"/><ellipse cx="12" cy="12" rx="4" ry="9"/><line x1="3" y1="12" x2="21" y2="12"/><line x1="5" y1="7" x2="19" y2="7"/><line x1="5" y1="17" x2="19" y2="17"/></svg>
        <span>www.dorlinagency.example,</span>
      </li>
      <li>
        <svg viewBox="0 0 24 24" aria-hidden="true"><path d="M12 3 2 12h3v8h5v-5h4v5h5v-8h3z"/></svg>
        <span>4375 West Tamber Lane</span>
      </li>
      <li class="indent"><span>Brenton Falls, Vermont 45192</span></li>
    </ul>
    <div class="social-links" aria-label="Social profiles">
      <span></span><span></span><span></span>
    </div>
  </div>
</body>
</html>
```